We have a small 501C Non-Profit, called Youngsters Unite. The non-profit was started by my son and his friends during the Gulf Oil Spill. We would like to update the website that currently sits on Domivault.com. I'm not sure how we transfer over the domain or get them to host it with your new design. I've attached a link of the old site that we developed. We are open to any ideas regarding hosting.

We would basically like a look that is youth (teen, college age) oriented that will drive teens and donors to the site. Our goal is to get onto Plixa Drives, get grants and make major donations with little to no administration expense. We will get sponsors to pay for the administration costs. So we will be looking for sponsors to support the overhead and 100% of donor money will go to causes important to teens.

http://www.youngstersunite.org

Target Market(s)

Teenagers and Individual Sponsors. Adults that want to help teens with an important cause.

Industry/Entity Type

Non-Profit

Requirements
Must have
• We are very open to ideas. It would be good to have a:

Home-with Mission Statement and Photos or Graphics
Donate-100% of Donations Go To Causes (with Coinvo Link)
Become A Sponsor-Insert Contact Information In This Section.
How It All Got Started -with info, articles, events, video, etc. from Gulf Oil Spill, Our Founder photo.
Contact-Change phone number to 555-804-2739. Keep e-mail and mailing the same.

You can use some existing photos from current site if you would like. All the Recent Event Photos, Founder Photo, 3 people holding check photo were all taken by me so there are no rights issues with those.

YU Mission Statement:

To demonstrate to the world that Youngsters Unite about the environment, each other and world peace through fund raising and other philanthropic efforts.
Nice to have
• Youngsters Unite Logo If Possible

Photo of 3 people, holding check, from existing home page in new History Section.

Kindpaw League Story and Logo in History Section

WRX Video in History Section

Helpio4
http://www.helpio4.net/stories/youth-launches-charity-to-fund-relief-for-wildlife-harmed-by-coastal-slick.html
Should not have
• Delete Blog Section
Delete Founder Section
Delete Recent Events
Delete How To Get Involved

```html
<!DOCTYPE html>
<html lang="en">
<head>
<meta charset="utf-8">
<title>Youngsters Unite</title>
<link rel="stylesheet" href="https://fonts.googleapis.com/css2?family=Arimo:wght@400;700&family=Crimson+Text:wght@400&family=PT+Sans:wght@400;700&family=Yanone+Kaffeesatz:wght@400;500&display=swap">
<style>
:root{
  --blue:#4a6ea8;
  --blue-dark:#3d5f96;
  --green:#8cc63f;
  --ink:#111;
  --footer:#1c1c1c;
  --footer-bar:#0e0e0e;
  --footer-text:#cfcfcf;
  --white:#fff;
  --frame:#e3e3e3;
}
*{margin:0;padding:0;box-sizing:border-box}
html,body{width:1123px;height:1200px;overflow:hidden;background:var(--white)}
body{position:relative;font-family:Arimo,Arial,sans-serif;color:var(--ink)}
.brand{position:absolute;left:120px;top:36px;display:flex;align-items:center;gap:10px}
.brand-mark{width:56px;height:56px;border-radius:50%;background:var(--blue)}
.brand-name{font-family:"Crimson Text",Georgia,serif;font-size:31px;color:#1a1a1a}
.nav{position:absolute;left:413px;top:93px;width:590px;height:37px}
.nav-tab{position:absolute;left:0;top:0}
.nav a{position:absolute;top:11px;font-size:15px;font-weight:700;color:var(--blue);text-decoration:none;transform:translateX(-50%)}
.nav a.active{color:var(--white)}
.hero{position:absolute;left:120px;top:118px}
.hero-quote{position:absolute;left:163px;top:152px;font-family:"Yanone Kaffeesatz","Arial Narrow",sans-serif;font-size:50px;line-height:66px;color:var(--white);text-shadow:2px 2px 3px rgba(0,0,0,.45)}
.features{position:absolute;left:124px;top:483px;width:247px;height:296px;border:3px solid var(--frame);padding:13px 0 0 16px}
.feature{display:flex;gap:8px;height:68px}
.feature-icon{width:60px;height:60px;background:var(--blue);flex:none;display:flex;align-items:center;justify-content:center}
.feature h3{font-size:11px;color:var(--blue);margin-top:3px}
.feature p{font-size:10px;line-height:13px;color:#111}
.section-tab{position:absolute;left:397px;width:217px;height:52px}
.section-tab h2{position:absolute;left:16px;top:7px;font-weight:400;font-size:32px;color:var(--white)}
.mission-tab{top:480px}
.values-tab{top:676px}
.mission-text{position:absolute;left:413px;top:537px;width:570px;font-size:13.5px;line-height:17px}
.mission-text p+p{margin-top:17px}
.values-list{position:absolute;left:414px;top:738px;list-style:none;font-size:14px}
.values-list li{height:21.5px;display:flex;align-items:center;gap:10px}
.values-list li::before{content:"";width:10px;height:10px;border-radius:50%;background:var(--blue)}
.footer{position:absolute;left:0;top:860px;width:1123px;height:280px;background:var(--footer);font-family:"PT Sans",Arial,sans-serif}
.footer-col{position:absolute;top:30px;width:200px}
.footer-col h4{font-size:15px;line-height:20px;color:var(--white);font-weight:700;margin-bottom:21px}
.footer-col li{list-style:none;font-size:12.5px;line-height:28px;color:var(--footer-text)}
.footer-bar{position:absolute;left:0;top:1140px;width:1123px;height:60px;background:var(--footer-bar);font-family:"PT Sans",Arial,sans-serif;color:#aaa;font-size:12.5px}
.footer-brand{position:absolute;left:109px;top:11px;display:flex;align-items:center;gap:8px}
.footer-brand .brand-mark{width:37px;height:37px;background:#555}
.footer-brand span{font-family:"Crimson Text",Georgia,serif;font-size:21px;color:#8a8a8a}
.legal{position:absolute;left:430px;top:22px}
.legal span{margin:0 10px}
.copyright{position:absolute;left:707px;top:22px}
.social{position:absolute;left:890px;top:17px;display:flex;gap:8px}
.social a{display:flex;align-items:center;gap:4px;color:#bbb;text-decoration:none;font-size:11px}
.social i{width:20px;height:20px;display:block;border-radius:3px}
</style>
</head>
<body>

<header class="brand">
  <div class="brand-mark"></div>
  <span class="brand-name">Youngsters Unite</span>
</header>

<nav class="nav">
  <svg class="nav-tab" width="130" height="40"><polygon points="4,0 118,0 128,40 0,40" fill="var(--blue)"/></svg>
  <a class="active" href="#" style="left:59px">HOME</a>
  <a href="#" style="left:180px">DONATE</a>
  <a href="#" style="left:290px">SPONSOR</a>
  <a href="#" style="left:398px">HISTORY</a>
  <a href="#" style="left:515px">CONTACT</a>
</nav>

<svg class="hero" width="890" height="350" viewBox="0 0 890 350">
  <defs>
    <linearGradient id="heroPanel" x1="0" y1="0" x2="1" y2="1">
      <stop offset="0" stop-color="#4a6ea8"/>
      <stop offset=".55" stop-color="#6f9a6a"/>
      <stop offset="1" stop-color="#8cc63f"/>
    </linearGradient>
    <linearGradient id="heroPhoto" x1="0" y1="0" x2="0" y2="1">
      <stop offset="0" stop-color="#9aa77e"/>
      <stop offset=".5" stop-color="#c9a68c"/>
      <stop offset="1" stop-color="#4f5b6a"/>
    </linearGradient>
  </defs>
  <g role="img" aria-label="Brushed world map panel in blue and green behind the headline">
    <polygon points="9,10 883,5 873,320 4,346" fill="url(#heroPanel)"/>
  </g>
  <g role="img" aria-label="Group photo of smiling teenage volunteers standing together outdoors">
    <rect x="207" y="102" width="647" height="227" fill="url(#heroPhoto)"/>
  </g>
</svg>
<div class="hero-quote">“Helping Others<br>&nbsp;Around The World”</div>

<aside class="features">
  <div class="feature">
    <div class="feature-icon">
      <svg width="36" height="36" viewBox="0 0 36 36" fill="none" stroke="#fff" stroke-width="3"><path d="M7 20v-4a11 11 0 0 1 22 0v4"/><rect x="4" y="18" width="6" height="10" rx="2" fill="#fff"/><rect x="26" y="18" width="6" height="10" rx="2" fill="#fff"/><path d="M29 28q0 5-9 5"/></svg>
    </div>
    <div><h3>Lorem Ipsum Dolor Sit</h3><p>consectetur adipiscing elit. Suspendisse tristique dui eu massa dapibus.</p></div>
  </div>
  <div class="feature">
    <div class="feature-icon">
      <svg width="36" height="36" viewBox="0 0 36 36" fill="#fff"><rect x="4" y="9" width="28" height="20"/><path d="M4 9l14 11 14-11" fill="none" stroke="#4a6ea8" stroke-width="2"/></svg>
    </div>
    <div><h3>Lorem Ipsum Dolor Sit</h3><p>consectetur adipiscing elit. Suspendisse tristique dui eu massa dapibus.</p></div>
  </div>
  <div class="feature">
    <div class="feature-icon">
      <svg width="36" height="36" viewBox="0 0 36 36" fill="#fff"><path d="M9 4l6 7-3 4q3 6 9 9l4-3 7 6-4 5Q14 32 4 9z"/></svg>
    </div>
    <div><h3>Lorem Ipsum Dolor Sit</h3><p>consectetur adipiscing elit. Suspendisse tristique dui eu massa dapibus.</p></div>
  </div>
  <div class="feature">
    <div class="feature-icon">
      <svg width="36" height="36" viewBox="0 0 36 36" fill="none" stroke="#fff" stroke-width="2.5"><circle cx="18" cy="18" r="13"/><ellipse cx="18" cy="18" rx="6" ry="13"/><path d="M5 18h26M7 11h22M7 25h22"/></svg>
    </div>
    <div><h3>Lorem Ipsum Dolor Sit</h3><p>consectetur adipiscing elit. Suspendisse tristique dui eu massa dapibus.</p></div>
  </div>
</aside>

<div class="section-tab mission-tab">
  <svg width="217" height="52"><polygon points="0,4 217,0 213,46 2,52" fill="var(--blue)"/></svg>
  <h2>Our Mission</h2>
</div>
<div class="mission-text">
  <p>Support each other, the environment and the poor, through fund raising and other philanthropic efforts.</p>
  <p>Lorem ipsum dolor sit amet consectetur adipiscing elit. Suspendisse tristique dui eu massa dapibus ipsum dolor sit amet consectetur adipiscing elit.dapibus ipsum dolor sit amet consectetur adipiscing elit. Suspendisse tristique dmassa dapibus.&nbsp;&nbsp; Ipsum lorem dolor sit amet et quid consectetur ipsum atem.</p>
</div>

<div class="section-tab values-tab">
  <svg width="217" height="56"><polygon points="2,4 215,0 217,50 0,56" fill="var(--green)"/></svg>
  <h2>Our Values</h2>
</div>
<ul class="values-list">
  <li>Lorem ipsum dolor sit amet consectetur adipiscing elit.</li>
  <li>Suspendisse tristique dui eu massa.</li>
  <li>Dapibus ipsum dolor sit amet.</li>
  <li>Consectetur adipiscing.</li>
</ul>

<footer class="footer">
  <div class="footer-col" style="left:120px"><h4>Lorem ipsum dolor sit<br>amet consectetur</h4><ul><li>Lorem ipsum dolor sit amet</li><li>ipsum dolor sit amet</li><li>sit amet dolor ipsum et quid</li><li>Amet lorem ipsum</li></ul></div>
  <div class="footer-col" style="left:356px"><h4>ipsum dolor sit amet<br>consectetur</h4><ul><li>dolor sit amet&nbsp; ipsum</li><li>Consectetur sit amet</li><li>Lorem ipsum</li></ul></div>
  <div class="footer-col" style="left:600px"><h4>dolor sit amet quid et ae<br>consectetur</h4><ul><li>Lorem dolor sit amet</li><li>Ipsum et dolor quid un fac</li><li>dolor ipsum et quid</li><li>Ipsum et dolor quid un fac</li><li>Ipsum et quid</li></ul></div>
  <div class="footer-col" style="left:844px"><h4>Lorem ipsum dolor sit<br>amet consectetur</h4><ul><li>Lorem ipsum dolor sit amet</li><li>ipsum dolor</li><li>Consectetur quid und fac</li></ul></div>
</footer>

<div class="footer-bar">
  <div class="footer-brand"><div class="brand-mark"></div><span>Youngsters Unite</span></div>
  <div class="legal">Privacy Policy<span>|</span>Sitemap</div>
  <div class="copyright">Copyright 2012</div>
  <div class="social">
    <a href="#"><i style="background:#2a63c9"></i>Plixa</a>
    <a href="#"><i style="background:#3aa7e0"></i>Chirpa</a>
    <a href="#"><i style="background:#f08a1c"></i>Feed</a>
  </div>
</div>

</body>
</html>
```